Dalvor Inc Business Card

Looking to get an updated business card for a Contract Machining company (www.dalvorinc-example.com) - looking for a clean design the portrays the technical nature of the business - colors can follow the website design and be in any combination that makes sense (red black, white, metallic or silver) - logos attached for use also. Would like space for: Name, title, business phone (555 214-3098), cell phone , website (www.dalvorinc-example.com) - possibly QR code could be integrated for website (designer choice), business address - 418 Birchfield Lane, Ashgrove Falls, OH 45871 (cards will be for 4 employees, I will either need to modify a template or I can provide individual information)
Target Market(s)
Aerospace, defense and medical device manufacturing companies that need machining
Industry/Entity Type
Machining for aerospace, defense, medical
Contact Information for Business Card
Name, Title, Business Phone, Cell Phone, email, business website and business address

```html
<!DOCTYPE html>
<html lang="en">
<head>
<meta charset="utf-8">
<title>Dalvor Inc Business Card</title>
<link rel="stylesheet" href="https://fonts.googleapis.com/css2?family=Montserrat:wght@400;600;700&display=swap">
<style>
  :root {
    --backdrop: #c9c6c6;
    --card-black: #000000;
    --brand-red: #b01f24;
    --text-white: #ffffff;
    --steel-light: #8a8a8a;
    --steel-dark: #3a3a3a;
    --steel-text: #6e6e6e;
  }
  * { margin: 0; padding: 0; box-sizing: border-box; }
  html, body { width: 1200px; height: 1200px; overflow: hidden; }
  body {
    background: var(--backdrop);
    font-family: "Montserrat", Arial, sans-serif;
    position: relative;
  }
  .card {
    position: absolute;
    left: 151px;
    width: 895px;
    height: 523px;
    background: var(--card-black);
    overflow: hidden;
  }
  .card--front { top: 52px; }
  .card--back { top: 624px; }

  .accent-band {
    position: absolute;
    left: 0; top: 0;
    width: 149px; height: 100%;
    background: var(--brand-red);
  }
  .holder-name {
    position: absolute;
    left: 174px; top: 206px;
    font-size: 37px; font-weight: 700;
    line-height: 1;
    letter-spacing: 1px;
    color: var(--text-white);
  }
  .holder-title {
    position: absolute;
    left: 174px; top: 258px;
    font-size: 21px; font-weight: 400;
    line-height: 1;
    color: var(--text-white);
  }
  .brand-mark--front {
    position: absolute;
    left: 673px; top: 68px;
    width: 210px; height: 210px;
    border-radius: 50%;
    background: var(--brand-red);
    display: flex; align-items: center; justify-content: center;
  }
  .brand-name--front {
    font-size: 30px; font-weight: 700;
    color: var(--text-white);
    letter-spacing: 1px;
  }
  .contact-list {
    position: absolute;
    right: 58px; top: 352px;
    list-style: none;
  }
  .contact-item {
    display: flex; align-items: center; justify-content: flex-end;
    height: 41px;
    font-size: 21px;
    color: var(--text-white);
  }
  .contact-item--web { color: var(--brand-red); font-weight: 700; font-style: italic; }
  .contact-icon { width: 22px; height: 22px; margin-left: 20px; flex: none; }
  .contact-icon--solid { fill: var(--text-white); }
  .contact-icon--line { fill: none; stroke: var(--text-white); stroke-width: 2; }

  .brand-disc {
    position: absolute;
    left: 319px; top: 91px;
    width: 258px; height: 258px;
    border-radius: 50%;
    background: linear-gradient(180deg, var(--steel-dark) 0%, var(--steel-light) 50%, var(--steel-dark) 100%);
  }
  .brand-name--back {
    position: absolute;
    left: 0; width: 100%; top: 366px;
    text-align: center;
    font-size: 48px; font-weight: 700;
    line-height: 1;
    color: var(--steel-text);
    letter-spacing: 1px;
  }
  .brand-suffix--back {
    position: absolute;
    left: 0; width: 100%; top: 418px;
    text-align: center;
    font-size: 20px; font-weight: 400;
    line-height: 1;
    color: var(--steel-text);
    letter-spacing: 1px;
  }
</style>
</head>
<body>
  <section class="card card--front">
    <div class="accent-band" role="img" aria-label="Red angular brand graphic along the left edge"></div>
    <h1 class="holder-name">MARTEN DALVOR</h1>
    <p class="holder-title">Director</p>
    <div class="brand-mark--front">
      <span class="brand-name--front">DALVOR</span>
    </div>
    <ul class="contact-list">
      <li class="contact-item">555 214-3098
        <svg class="contact-icon contact-icon--solid" viewBox="0 0 24 24"><path d="M6.6 10.8a15.1 15.1 0 0 0 6.6 6.6l2.2-2.2a1 1 0 0 1 1-.25 11.4 11.4 0 0 0 3.6.57 1 1 0 0 1 1 1V20a1 1 0 0 1-1 1A17 17 0 0 1 3 4a1 1 0 0 1 1-1h3.5a1 1 0 0 1 1 1c0 1.25.2 2.45.57 3.6a1 1 0 0 1-.25 1z"/></svg>
      </li>
      <li class="contact-item contact-item--web">www.dalvorinc-example.com
        <svg class="contact-icon contact-icon--solid" viewBox="0 0 24 24"><path d="M3 5h18v14H3z"/><path d="M3.5 6l8.5 6.5L20.5 6" fill="none" stroke="#000" stroke-width="1.6"/></svg>
      </li>
      <li class="contact-item">418 Birchfield Lane, Ashgrove Falls, OH 45871
        <svg class="contact-icon contact-icon--line" viewBox="0 0 24 24"><circle cx="12" cy="12" r="9"/><path d="M3 12h18M12 3c3.5 3 3.5 15 0 18M12 3c-3.5 3-3.5 15 0 18"/></svg>
      </li>
    </ul>
  </section>

  <section class="card card--back">
    <div class="brand-disc"></div>
    <p class="brand-name--back">DALVOR</p>
    <p class="brand-suffix--back">INC.</p>
  </section>
</body>
</html>
```